Financial Broker firm looking for Brochure design/Pdf-document

Job Type
Brochure Design/PDF-Document
Task Outline
Create a Brochure Design that also works for sending as pdf-document.
Task Description
We need a combined corporate brochure (Booklet style) to give out to potential clients as well as sending it to potential clients through Internet as pdf-document.
We need a background template with pictures and colors that gives the impression of professionalism, trustworthiness and seriousness. Attached text in English but the text will be translated into different languages to fit different markets. Therefore we would like to receive one template including the text and one without any text (but with the logo). Please inform us where (any) pictures and/or photos on the template have been taken from in order for us to buy and use them legally.
About Us
Our company Kelvora Trust AB is a financial brokerage company who provides a diversity of services for different selected partners (www.kelvoratrust.example).
Target Market
Companies on all levels, domestic or international
Requirements
Must Have:
-The text and logo attached below
Industry/Entity Type
Financial
Look and feel

```html
<!DOCTYPE html>
<html lang="en">
<head>
<meta charset="utf-8">
<title>Kelvora Trust – Brochure Spread</title>
<link rel="stylesheet" href="https://fonts.googleapis.com/css2?family=Roboto:wght@300;400;700&family=Arimo:wght@400;700&display=swap">
<style>
  :root {
    --page-bg: #ffffff;
    --ink: #111111;
    --ink-soft: #222222;
    --title-grey: #444444;
    --bar-grey: #cccccc;
    --navy: #0b1a30;
    --night: #07090c;
    --cyan: #19e3ee;
    --panel-text: #c8ccd2;
    --edge: #9a9a9a;
  }
  * { box-sizing: border-box; margin: 0; padding: 0; }
  html, body { width: 1200px; height: 1000px; overflow: hidden; background: var(--page-bg); }
  body { position: relative; font-family: "Arimo", Arial, sans-serif; color: var(--ink); }

  .spread {
    position: absolute; left: 135px; top: 153px; width: 932px; height: 698px;
    border: 1px solid var(--edge); background: var(--page-bg);
    box-shadow: 0 6px 18px rgba(0,0,0,0.18);
  }
  .page-divider { position: absolute; left: 465px; top: 0; width: 1px; height: 100%; background: #bdbdbd; }

  /* Left page */
  .brand {
    position: absolute; left: 57px; top: 64px;
    font-family: "Roboto", Arial, sans-serif; font-weight: 700; font-size: 33px;
    letter-spacing: 0.5px; color: var(--ink);
  }
  .intro {
    position: absolute; left: 58px; top: 125px; width: 361px;
    font-size: 13.6px; line-height: 18.9px; text-align: justify; color: var(--ink-soft);
  }
  .services-title {
    position: absolute; left: 73px; top: 396px;
    font-family: "Roboto", Arial, sans-serif; font-size: 40px; line-height: 46px; color: var(--title-grey);
  }
  .services-title strong { font-weight: 700; }
  .services-title span { font-weight: 400; color: #333; }
  .service-list { list-style: none; position: absolute; left: 64px; top: 451px; width: 350px; }
  .service-item {
    position: absolute; left: 0; width: 350px; height: 29px; background: var(--bar-grey);
    font-size: 15.5px; line-height: 29px; padding-left: 25px; color: var(--ink-soft);
  }
  .service-item::before {
    content: ""; position: absolute; left: 6px; top: 11px; width: 6px; height: 6px;
    border-radius: 50%; background: var(--ink);
  }

  /* Right page */
  .section-tab {
    position: absolute; left: 466px; top: 64px; width: 332px; height: 59px; background: var(--navy);
    font-family: "Roboto", Arial, sans-serif; font-size: 23px; line-height: 59px; padding-left: 26px; color: var(--cyan);
  }
  .section-tab strong { font-weight: 700; }
  .section-tab span { font-weight: 300; }
  .rule-band { position: absolute; left: 466px; top: 123px; width: 466px; height: 7px; background: var(--bar-grey); }
  .hero-photo { position: absolute; left: 466px; top: 130px; width: 466px; height: 349px; }
  .info-panel {
    position: absolute; left: 466px; top: 479px; width: 466px; height: 178px; background: var(--night);
    padding: 23px 69px 0 43px;
    font-family: "Roboto", Arial, sans-serif; font-weight: 300; font-size: 13.6px; line-height: 20px;
    text-align: justify; color: var(--panel-text);
  }
  .footer-band { position: absolute; left: 466px; top: 657px; width: 466px; height: 41px; background: var(--bar-grey); }
</style>
</head>
<body>
  <main class="spread">
    <div class="page-divider"></div>

    <section class="page page-left">
      <div class="brand">KELVORA TRUST</div>
      <p class="intro">As a finance broker based in Sweden, we market a diversity of services in order for you to improve your company's finances and at the same time lowering your company's cost. Through our partners, we will assist you to find the right solution, which includes best price and quality to fit your needs and demands. Our goal is customer satisfactory, our service is for free and our aim is through the knowledge and expertise we, we can build a strong long and lasting business relationship together. With Kelvora Trust you will have your own personal account manager (or reseller contact) that speaks the language you understand in order to take advantage of the services our partners provide. We are regulated by the Swedish financial inspection.</p>

      <h2 class="services-title"><strong>Our</strong><span>services</span></h2>
      <ul class="service-list">
        <li class="service-item" style="top:0">Foreign exchange service</li>
        <li class="service-item" style="top:34px">Covering financial risks</li>
        <li class="service-item" style="top:68px">Trade credit insurance</li>
        <li class="service-item" style="top:105px">Bonding</li>
        <li class="service-item" style="top:139px">Trade debt collections</li>
        <li class="service-item" style="top:173px">Factoring</li>
      </ul>
    </section>

    <section class="page page-right">
      <h2 class="section-tab"><strong>Foreign exchange</strong> <span>service</span></h2>
      <div class="rule-band"></div>
      <svg class="hero-photo" role="img" aria-label="Photo of a businessman in a suit pointing at a glowing financial growth chart" viewBox="0 0 466 349" preserveAspectRatio="none">
        <defs>
          <radialGradient id="heroGlow" cx="0.4" cy="0.55" r="0.75">
            <stop offset="0" stop-color="#2c4f86"/>
            <stop offset="0.55" stop-color="#15294a"/>
            <stop offset="1" stop-color="#070b14"/>
          </radialGradient>
        </defs>
        <rect width="466" height="349" fill="url(#heroGlow)"/>
      </svg>
      <p class="info-panel">If your company trades internationally, you are more than likely to make international payments. Our partners will help your company manage this process. You can save half the costs involved in the money transfer and get access to a better service compared to traditional banks.</p>
      <div class="footer-band"></div>
    </section>
  </main>
</body>
</html>
```